Your conflict - our mediation - joint conflict SOLUTION

With this flyer I am looking for conflict parties who are ready to tackle and resolve their conflict with a prospective mediator. The mediation is free because I am doing it as part of my diploma thesis. Time frame approx. 4 sessions of 2.5 hours each. The wishes and needs of both parties are listened to and “picked out”. In an open, constructive, appreciative framework, solutions are developed and negotiated together.

Target Market(s)

everyone who is ready to deal with himself and his counterpart and everyone who wants to work out a solution with the respect, openness and support of a mediator.

Requirements
Must have
• - "For my diploma thesis I am looking for conflicting parties who are willing to resolve their conflict with a mediator"
- Time frame: 4 x 2.5 hours feasible in Solothurn, Bern, Brugg
- Free of charge
- my coordinates - see business card
- more information at www.talweidenhof.ch
Nice to have
• the card should be based on the style of my homepage www.talweidenhof.ch and my business card

```html
<!DOCTYPE html>
<html lang="de">
<head>
<meta charset="utf-8">
<title>Ihr Konflikt – Unsere Mediation</title>
<link rel="stylesheet" href="https://fonts.googleapis.com/css2?family=Montserrat:wght@300;400;500;600;800&family=Oswald:wght@500;600&display=swap">
<style>
  :root {
    --paper: #ffffff;
    --gold: #a88a5a;
    --teal: #1d5573;
    --teal-dark: #1d4e6b;
    --green: #17704a;
    --ink: #222222;
    --purple: #4a3566;
    --red: #d01e24;
    --brush: #2b3a8c;
    --rule: #b9b9b9;
    --photo-a: #2a3242;
    --photo-b: #8f7358;
  }
  * { margin: 0; padding: 0; box-sizing: border-box; }
  html, body { width: 800px; height: 1200px; overflow: hidden; background: var(--paper); }
  .flyer { position: relative; width: 800px; height: 1200px; background: var(--paper); font-family: "Montserrat", sans-serif; }

  .hero { position: absolute; left: 0; top: 0; width: 800px; height: 450px; }

  .brand-badge {
    position: absolute; left: 56px; top: 110px; width: 264px; height: 264px;
    border-radius: 50%; background: var(--paper); border: 6px solid var(--teal-dark);
    display: flex; align-items: center; justify-content: center;
    box-shadow: 0 4px 10px rgba(0,0,0,.12);
  }
  .brand-name { font-weight: 600; font-size: 30px; color: var(--gold); letter-spacing: .5px; }

  .headline { position: absolute; left: 0; width: 800px; text-align: center; line-height: 1; white-space: nowrap; }
  .headline-conflict { top: 455px; font-weight: 300; font-size: 86px; color: var(--gold); }
  .headline-mediation { top: 527px; font-weight: 800; font-size: 62px; color: var(--teal); }
  .headline-solution { top: 585px; font-weight: 800; font-size: 35px; color: var(--green); letter-spacing: 2.6px; }

  .rule { position: absolute; left: 62px; top: 632px; width: 694px; height: 3px; background: var(--rule); }

  .intro {
    position: absolute; left: 0; top: 641px; width: 800px; text-align: center;
    font-weight: 500; font-size: 29px; line-height: 33px; color: var(--ink);
  }

  .fact {
    position: absolute; top: 788px; height: 78px;
    border: 3px solid var(--gold); border-radius: 39px 14px 14px 39px;
    display: flex; align-items: center;
  }
  .fact-duration { left: 71px; width: 367px; }
  .fact-place { left: 472px; width: 270px; }
  .fact-icon {
    width: 78px; height: 78px; margin-left: -3px; border-radius: 50%;
    background: var(--purple); border: 4px solid #d9cfe4;
    display: flex; align-items: center; justify-content: center; flex: none;
  }
  .fact-figure { font-family: "Oswald", sans-serif; font-weight: 600; font-size: 50px; color: var(--green); margin-left: 18px; letter-spacing: 1px; }
  .fact-label { font-weight: 400; font-size: 21px; line-height: 21px; color: var(--ink); margin-left: 10px; text-transform: uppercase; }
  .fact-place .fact-label { text-transform: none; font-size: 20px; margin-left: 16px; }

  .offer {
    position: absolute; left: 60px; top: 920px; width: 679px; height: 170px;
    border: 3px solid var(--gold); border-radius: 24px 24px 0 0; overflow: hidden;
  }
  .offer-title {
    position: absolute; left: 0; top: 12px; width: 100%; text-align: center;
    font-family: "Oswald", sans-serif; font-weight: 600; font-size: 94px; line-height: 1;
    letter-spacing: -1px; white-space: nowrap;
    transform: scaleY(1.1); transform-origin: center top;
  }
  .offer-free { color: var(--red); }
  .offer-charge { color: var(--purple); }
  .offer-link {
    position: absolute; left: 0; bottom: 0; width: 100%; height: 46px;
    background: var(--teal); color: #fff; font-size: 23px; font-weight: 400;
    display: flex; align-items: center; justify-content: center;
  }
  .offer-link strong { font-weight: 800; }
</style>
</head>
<body>
<main class="flyer">
  <svg class="hero" viewBox="0 0 800 450">
    <defs>
      <linearGradient id="photoTone" x1="0" y1="0" x2="0.6" y2="1">
        <stop offset="0" stop-color="#2a3242"/>
        <stop offset="0.6" stop-color="#4a4a52"/>
        <stop offset="1" stop-color="#8f7358"/>
      </linearGradient>
    </defs>
    <path role="img" aria-label="Photo: a person in a suit stacking wooden blocks beneath a small wooden house"
          d="M136 0 H800 V250 Q740 400 560 428 Q360 450 230 345 Q150 250 136 0 Z"
          fill="url(#photoTone)"/>
    <path d="M136 0 Q138 40 150 80" fill="none" stroke="#1d4e6b" stroke-width="12" stroke-linecap="round"/>
    <path d="M290 395 Q430 460 600 420 Q730 385 800 262" fill="none" stroke="#2b3a8c" stroke-width="14" stroke-linecap="round"/>
  </svg>

  <div class="brand-badge">
    <span class="brand-name">Talweidenhof</span>
  </div>

  <h1 class="headline headline-conflict">IHR KONFLIKT</h1>
  <h2 class="headline headline-mediation">UNSERE MEDIATION</h2>
  <h3 class="headline headline-solution">GEMEINSAME KONFLIKTLÖSUNG</h3>
  <div class="rule"></div>

  <p class="intro">For my diploma thesis I am looking<br>for conflicting parties who are willing to<br>resolve their conflict with a mediator</p>

  <div class="fact fact-duration">
    <div class="fact-icon">
      <svg width="40" height="40" viewBox="0 0 40 40" fill="none" stroke="#fff" stroke-width="2.4" stroke-linecap="round">
        <circle cx="22" cy="23" r="11"/>
        <path d="M22 23 V17 M22 23 L26 26 M19 8 H25 M22 8 V12 M4 19 H9 M3 24 H9 M5 29 H10"/>
      </svg>
    </div>
    <span class="fact-figure">4 X 2.5</span>
    <span class="fact-label">Hours<br>Feasible</span>
  </div>

  <div class="fact fact-place">
    <div class="fact-icon">
      <svg width="40" height="40" viewBox="0 0 40 40" fill="none" stroke="#fff" stroke-width="2.6" stroke-linecap="round" stroke-linejoin="round">
        <path d="M20 33 C12 24 10 20 10 16 A10 10 0 0 1 30 16 C30 20 28 24 20 33 Z"/>
        <circle cx="20" cy="16" r="3.5"/>
        <path d="M8 34 H32"/>
      </svg>
    </div>
    <span class="fact-label">in Solothurn,<br>Bern, Brugg</span>
  </div>

  <section class="offer">
    <p class="offer-title"><span class="offer-free">FREE</span> <span class="offer-charge">OF CHARGE</span></p>
    <p class="offer-link">For more information at&nbsp;www.<strong>talweidenhof</strong>.ch</p>
  </section>
</main>
</body>
</html>
```